IT Company needs full suite of stationery

Our company 4027 Veltrane Partners Inc. is an IT company based in Toronto, Canada. Based on our logo we would like to see business cards(front and back), letterhead, envelope, brochure template. Design would be simple, not too bright, modern but can be used for many years, good theme throughout. Our official logo is the the fullcolor_a, full company name is 4027 Veltrane Partners Inc., Please include full company name on all pieces. Logo can be modified to be the graphic only with the "4027 Partners", I have cropped it myself for a couple files but I am no designer. We will provide lots of feedback so post early and often.
Updates

Reason: Very busy around the holidays, like a lot of the designs currently submitted, will definitely be picking one. Thanks for your submissions and merry Christmas and Happy New Year to everyone.

Industry/Entity Type

Business

```html
<!DOCTYPE html>
<html lang="en">
<head>
<meta charset="utf-8">
<title>4027 Veltrane Partners Inc. — Stationery Suite</title>
<link href="https://fonts.googleapis.com/css2?family=Source+Sans+3:ital,wght@0,400;0,600;0,700;1,400&display=swap" rel="stylesheet">
<style>
:root{
  --green:#2e9a45;
  --green-light:#7ab83c;
  --green-dark:#1f8a3e;
  --ink:#222;
  --charcoal:#231f20;
  --grey:#4a4a4a;
  --paper:#fff;
  --faint-green:#dcebdc;
  --faint-grey:#dedede;
  --faint-name:#c9dfc6;
  --shadow:0 2px 6px rgba(0,0,0,.35);
}
*{box-sizing:border-box;margin:0;padding:0}
html,body{width:1200px;height:1000px;overflow:hidden;background:#fff}
body{font-family:"Source Sans 3",sans-serif;color:var(--ink);position:relative}
.label{position:absolute;font-style:italic;font-size:15px;color:#000;transform:translateX(-50%);white-space:nowrap;z-index:3}
.piece{position:absolute;overflow:hidden;box-shadow:var(--shadow);background:var(--paper);z-index:2}
.letterhead{z-index:1}
.card{border-radius:12px}
.grad{background:linear-gradient(180deg,var(--green-light),var(--green-dark))}
.seal{position:absolute;border-radius:50%;background:linear-gradient(180deg,var(--green-light),var(--green-dark))}
.seal.ringed{box-shadow:0 0 0 6px #fff,0 0 0 12px var(--green)}
.seal-name{position:absolute;color:#fff;font-weight:600;text-align:center;line-height:1.05;white-space:nowrap}
.logo{position:absolute;display:flex;align-items:center;gap:7px;white-space:nowrap}
.logo-dot{border-radius:50%;background:var(--green);flex:none}
.logo-name{font-weight:600;color:var(--grey);letter-spacing:.5px;line-height:1}
.logo.light .logo-dot{background:#fff}
.logo.light .logo-name{color:#fff}
.legal-name{position:absolute;color:#fff;font-weight:600;text-align:center;white-space:nowrap;letter-spacing:.5px}
.contact{position:absolute;line-height:1.3;color:#000}
.contact b{color:var(--green);font-weight:700}
.contact .company{font-weight:700;color:var(--grey)}
.person{color:var(--green);font-weight:700}
</style>
</head>
<body>

<!-- Letterhead (sits behind the smaller pieces) -->
<span class="label" style="left:918px;top:11px">Letter Head</span>
<div class="piece letterhead" style="left:659px;top:38px;width:516px;height:668px">
  <div class="logo" style="left:28px;top:42px"><span class="logo-dot" style="width:40px;height:40px"></span><span class="logo-name" style="font-size:22px">4027 Partners</span></div>
  <div class="contact" style="right:28px;top:22px;font-size:8.5px;text-align:right">
    <div class="company">4027 Veltrane Partners Inc.</div>
    <div><b>Telephone:</b> 0123456789</div>
    <div><b>Fax:</b> 0123456789</div>
    <div><b>Email:</b> info@4027partners.com</div>
    <div><b>Website:</b> www.4027partners.com</div>
    <div><b>Address:</b> abc street, Op. Xyz</div>
    <div>Building, City, County.</div>
  </div>
  <div style="position:absolute;left:98px;top:180px;width:336px;height:336px;border-radius:50%;border:8px solid var(--faint-green);background:linear-gradient(180deg,#eef6ea,var(--faint-grey));box-shadow:inset 0 0 0 10px #fff"></div>
  <div class="seal-name" style="left:98px;top:312px;width:336px;font-size:44px;color:var(--faint-name)">4027 Partners</div>
</div>

<!-- Business card front -->
<span class="label" style="left:203px;top:22px">Business Card Front</span>
<div class="piece card" style="left:33px;top:45px;width:355px;height:205px">
  <div class="seal ringed" style="left:210px;top:-5px;width:225px;height:225px"></div>
  <div class="seal-name" style="left:222px;top:78px;width:133px;font-size:24px">4027<br>Partners</div>
  <div class="logo" style="left:15px;top:34px"><span class="logo-dot" style="width:30px;height:30px"></span><span class="logo-name" style="font-size:17px">4027 Partners</span></div>
  <div class="contact" style="left:15px;top:90px;font-size:8px">
    <div class="person" style="font-size:11px">Your Name</div>
    <div>Designation</div>
    <div class="company" style="margin-top:4px">4027 Veltrane Partners Inc.</div>
    <div><b>Cell:</b> 0123456789</div>
    <div><b>Telephone:</b> 0123456789</div>
    <div><b>Fax:</b> 0123456789</div>
    <div><b>Email:</b> info@4027partners.com</div>
    <div><b>Website:</b> www.4027partners.com</div>
    <div><b>Address:</b> abc street, Op. Xyz Building, City, County.</div>
  </div>
</div>

<!-- Business card back 1 -->
<span class="label" style="left:211px;top:257px">Business Card Back option:1</span>
<div class="piece card grad" style="left:30px;top:280px;width:355px;height:202px">
  <div class="logo light" style="left:88px;top:70px"><span class="logo-dot" style="width:44px;height:44px"></span><span class="logo-name" style="font-size:24px">4027 Partners</span></div>
  <div class="legal-name" style="left:0;top:124px;width:355px;font-size:11px">4027 Veltrane Partners Inc.</div>
</div>

<!-- Business card back 2 -->
<span class="label" style="left:204px;top:487px">Business Card Back option:2</span>
<div class="piece card" style="left:30px;top:510px;width:355px;height:202px">
  <div role="img" aria-label="Light repeating company-name pattern" style="position:absolute;inset:0;background:linear-gradient(135deg,#f2f2f2,#e8f1e6)"></div>
  <div class="seal ringed" style="left:113px;top:47px;width:110px;height:110px"></div>
  <div class="seal-name" style="left:113px;top:83px;width:110px;font-size:17px">4027<br>Partners</div>
  <div class="legal-name" style="left:0;top:176px;width:355px;font-size:10px;color:var(--grey)">4027 Veltrane Partners Inc.</div>
</div>

<!-- Business card back 3 -->
<span class="label" style="left:204px;top:716px">Business Card Back option:3</span>
<div class="piece card" style="left:26px;top:736px;width:357px;height:202px;background:var(--charcoal)">
  <div class="logo light" style="left:88px;top:70px"><span class="logo-dot" style="width:44px;height:44px"></span><span class="logo-name" style="font-size:24px">4027 Partners</span></div>
  <div class="legal-name" style="left:0;top:124px;width:357px;font-size:11px">4027 Veltrane Partners Inc.</div>
</div>

<!-- CD -->
<span class="label" style="left:525px;top:22px">Cd</span>
<svg style="position:absolute;left:420px;top:40px;z-index:2" width="210" height="210" viewBox="0 0 210 210">
  <defs><linearGradient id="cdFill" x1="0" y1="0" x2="0" y2="1"><stop offset="0" stop-color="#7ab83c"/><stop offset="1" stop-color="#1f8a3e"/></linearGradient></defs>
  <circle cx="105" cy="105" r="101" fill="#fff" stroke="#2e9a45" stroke-width="5"/>
  <circle cx="105" cy="105" r="90" fill="url(#cdFill)"/>
  <text x="105" y="56" text-anchor="middle" font-size="17" font-weight="600" fill="#fff" font-family="Source Sans 3, sans-serif">4027 Partners</text>
  <circle cx="103" cy="105" r="31" fill="#fff" stroke="#111" stroke-width="4"/>
  <circle cx="103" cy="105" r="12" fill="#bbb"/>
  <text x="105" y="160" text-anchor="middle" font-size="8" font-weight="600" fill="#fff" font-family="Source Sans 3, sans-serif">4027 Veltrane Partners Inc.</text>
  <text x="105" y="173" text-anchor="middle" font-size="8" font-style="italic" fill="#cfe8c4" font-family="Source Sans 3, sans-serif">www.yourwebsite.com</text>
</svg>

<!-- CD cover -->
<span class="label" style="left:565px;top:241px">Cd Cover</span>
<div class="piece" style="left:458px;top:262px;width:229px;height:200px">
  <div style="position:absolute;left:0;top:0;width:100%;height:36px;background:var(--charcoal)"></div>
  <div class="seal ringed" style="left:98px;top:45px;width:165px;height:165px"></div>
  <div class="seal-name" style="left:104px;top:104px;width:125px;font-size:19px">4027<br>Partners</div>
  <div class="logo" style="left:10px;top:52px"><span class="logo-dot" style="width:18px;height:18px"></span><span class="logo-name" style="font-size:10px">4027 Partners</span></div>
  <div class="contact" style="left:8px;top:144px;font-size:5.5px">
    <div class="company">4027 Veltrane Partners Inc.</div>
    <div><b>Telephone:</b> 0123456789</div>
    <div><b>Fax:</b> 0123456789</div>
    <div><b>Email:</b> info@4027partners.com</div>
    <div><b>Website:</b> www.4027partners.com</div>
    <div><b>Address:</b> abc street, Op. Xyz Building,</div>
    <div>City, County.</div>
  </div>
</div>

<!-- Email signature -->
<span class="label" style="left:575px;top:470px">Email Signature</span>
<div class="piece" style="left:425px;top:492px;width:298px;height:143px">
  <div class="seal ringed" style="left:160px;top:8px;width:165px;height:165px"></div>
  <div class="seal-name" style="left:168px;top:52px;width:130px;font-size:19px">4027<br>Partners</div>
  <div class="logo" style="left:12px;top:15px"><span class="logo-dot" style="width:22px;height:22px"></span><span class="logo-name" style="font-size:12px">4027 Partners</span></div>
  <div class="contact" style="left:11px;top:58px;font-size:6.5px">
    <div class="person" style="font-size:8px">Your Name</div>
    <div>Designation</div>
    <div class="company" style="margin-top:3px">4027 Veltrane Partners Inc.</div>
    <div><b>Telephone:</b> 0123456789</div>
    <div><b>Fax:</b> 0123456789</div>
    <div><b>Email:</b> info@4027partners.com</div>
    <div><b>Website:</b> www.4027partners.com</div>
    <div><b>Address:</b> abc street, Op. Xyz Building, City, County.</div>
  </div>
</div>

<!-- Envelope back 1 -->
<span class="label" style="left:578px;top:647px">Envelope Back Option: 1</span>
<div class="piece grad" style="left:490px;top:670px;width:487px;height:80px">
  <div style="position:absolute;left:217px;top:10px;width:40px;height:40px;border-radius:50%;background:#fff;box-shadow:0 0 0 3px var(--green-dark)"></div>
</div>

<!-- Envelope back 2 -->
<div class="piece grad" style="left:410px;top:725px;width:487px;height:217px">
  <svg style="position:absolute;left:0;top:0" width="487" height="60" viewBox="0 0 487 60"><polygon points="0,0 487,0 487,10 447,55 40,55 0,10" fill="#231f20"/></svg>
  <div style="position:absolute;left:214px;top:8px;width:42px;height:42px;border-radius:50%;background:#fff;box-shadow:0 0 0 3px #231f20"></div>
</div>
<span class="label" style="left:492px;top:950px">Envelope Back Option: 2</span>

<!-- Envelope front -->
<span class="label" style="left:1033px;top:725px">Envelope Front</span>
<div class="piece" style="left:695px;top:748px;width:480px;height:215px">
  <div class="seal ringed" style="left:285px;top:-10px;width:280px;height:280px"></div>
  <div class="seal-name" style="left:300px;top:40px;width:180px;font-size:28px">4027<br>Partners</div>
  <div class="logo" style="left:18px;top:22px"><span class="logo-dot" style="width:38px;height:38px"></span><span class="logo-name" style="font-size:20px">4027 Partners</span></div>
  <div class="contact" style="left:18px;top:130px;font-size:8px">
    <div class="company">4027 Veltrane Partners Inc.</div>
    <div><b>Telephone:</b> 0123456789</div>
    <div><b>Fax:</b> 0123456789</div>
    <div><b>Email:</b> info@4027partners.com</div>
    <div><b>Website:</b> www.4027partners.com</div>
    <div><b>Address:</b> abc street, Op. Xyz Building, City, County.</div>
  </div>
  <div style="position:absolute;left:245px;top:129px;width:215px;height:66px;border-radius:8px;background:linear-gradient(180deg,#f4f4f4,#dcdcdc);border:1px solid #ccc"></div>
</div>

</body>
</html>
```